Branding product image: BUVESO (Golden Papaya) in Plastic Cup (Ready to Eat)

The product is sliced Fruit in Light syrup
Flavour: BUVESO (Golden Papaya)
The temporary product name: BUVESO
I want the product design to be something 'fun', 'natural', and 'colourful'
The design concept could be anything depends on your imagination, but it must be eye catchy and attractive.
Basically, I want you to be creative in designing the logo and the overall graphic design for the label.
The measurement is 20 cm (Length) x 6,5 cm (Height)
The target customers are young and health conscious audiences (10 years - 65 years old).
Create something different. Something extraordinary.
Brief summary about the fruit:
This fruit only grows in certain part of the world. It grows in mountain area that is in tropical climate. The fruit flesh has a yellowish-golden color. It has an extraordinary taste (unlike normal papaya) and it suits very well with any dishes from cold appetizer, white/ red meat, desserts, and cocktails.
I need a packaging design for Fruit Cup productThe product is sliced Fruit in Light syrup.There will be various flavours i.e. apple, lychee, peach, papaya, etc.However, you may design the product using one sample flavour (i.e. papaya) first, as the designs of other flavours could be adjusted afterwards.The temporary product name is: RICCANAI want the product design to be something 'fun', 'natural', and 'colourful'.The design concept could be anything depends on your imagination. Basically, I want you to be creative in designing the logo and the overall graphic design for the label. - Create something different. Something extraordinary -Additional:The measurement is 20cm (Length) x 5cm (Height).The target customers are young audiences (10 years - 35 years old).The product design must stand out in the supermarket shelf.It must be eye catchy and attractive.Thank you,Dorwin-PLEASE REFER TO DESIGN SAMPLE ATTACHED TO HAVE A BETTER UNDERSTANDING FOR THE PRODUCT CONCEPT- Added Wednesday, September 17, 2014
Project Deadline Extended Reason: Haven't found a good design. Added Friday, September 19, 2014
Project Deadline Extended Reason: Need more time for designers to finalize and perfect the design.Thank you,Dorwin Added Monday, September 29, 2014
Project Deadline Extended Reason: I haven't found a great design yet. Added Tuesday, February 24, 2015
Reason: Getting better designs now. Still Open to new ideas while refining the latest designs from some designers.
Please do your best in submitting other great designs!

```html
<!DOCTYPE html>
<html lang="en">
<head>
<meta charset="utf-8">
<title>TOMELDU Golden Papaya – Cup Lid</title>
<link rel="stylesheet" href="https://fonts.googleapis.com/css2?family=Oswald:wght@400;500;600&display=swap">
<style>
  :root {
    --backdrop: #e4e6e9;
    --lid: #f3f4f5;
    --lid-ring: #e2e4e7;
    --brand-orange: #e15812;
    --golden: #e9a114;
    --syrup-brown: #4a3b31;
    --papaya-light: #f6d23a;
    --papaya-deep: #e99a1c;
  }
  html, body {
    margin: 0;
    padding: 0;
    width: 1200px;
    height: 1200px;
    overflow: hidden;
    background: var(--backdrop);
  }
  .lid-label {
    display: block;
    width: 1200px;
    height: 1200px;
  }
  .lid-shape { fill: var(--lid); }
  .lid-ring { fill: none; stroke: var(--lid-ring); stroke-width: 6; }
  .brand-name {
    font-family: "Oswald", sans-serif;
    font-weight: 500;
    fill: var(--brand-orange);
  }
  .product-line {
    font-family: "Oswald", sans-serif;
    font-weight: 400;
    fill: var(--syrup-brown);
  }
  .flavour-name {
    font-family: "Oswald", sans-serif;
    font-weight: 500;
    fill: var(--golden);
  }
</style>
</head>
<body>
<svg class="lid-label" viewBox="0 0 1200 1200" xmlns="http://www.w3.org/2000/svg">
  <defs>
    <radialGradient id="papaya-tone" cx="55%" cy="45%" r="60%">
      <stop offset="0%" stop-color="var(--papaya-deep)"/>
      <stop offset="100%" stop-color="var(--papaya-light)"/>
    </radialGradient>
  </defs>

  <g class="lid">
    <rect class="lid-shape" x="62" y="712" width="160" height="298" rx="60"/>
    <circle class="lid-shape" cx="640" cy="600" r="540"/>
    <circle class="lid-ring" cx="640" cy="600" r="475"/>
  </g>

  <text class="brand-name" x="333" y="445" font-size="176" textLength="590" lengthAdjust="spacingAndGlyphs">TOMELDU</text>

  <text class="product-line" x="464" y="493" font-size="40" textLength="462" lengthAdjust="spacingAndGlyphs">FRESH FRUIT IN LIGHT SYRUP</text>

  <text class="flavour-name" x="336" y="711" font-size="240" textLength="594" lengthAdjust="spacingAndGlyphs">GOLDEN</text>

  <text class="flavour-name" x="336" y="898" font-size="188" textLength="415" lengthAdjust="spacingAndGlyphs">PAPAYA</text>

  <ellipse role="img" aria-label="Photo of a whole golden papaya beside a halved papaya showing seeds" cx="870" cy="822" rx="108" ry="84" fill="url(#papaya-tone)"/>
</svg>
</body>
</html>
```